High End Cosmetic Packaging Design Project

Looking for packaging for 2 products for a High end skin care line aimed at the 35+ year old women. Color scheme is Pantone 2765c with accents of metallic silver, copper or gold, Pantone colors 871-877c. Possible watermark in the background or a 3D image. We are open to any good ideas and suggestions. Box dimensions for the 2 products are small, approximately 4.375 inches high and 1.5 inches square. I have attached an image of the logo. I have the logo files in all the various forms. 1 box is for a Vitamin C Serum and the other box is for an Anti Aging Serum. Boxes are the same but the text will be different on both products. I will supply the text for the boxes later, including directions & ingredients and a UPC code that has to go on the underside of the box. It has to be an elegant design that will stand out in photos online. Good and quick communication & feedback between you and us is essential. I have attached a jpg of our new logo. I have this logo in all available forms
*****We are open to all ideas and want your ideas and input. The bottles that go inside these boxes are a deep violet almost black kovra glass. This is where the pantone color selection came from but upon further thought it may not be the right choice. We were out looking at cosmetic packaging today and thought also as an idea that a dark charcoal, or black box might work as well. We have seen boxes in those dark shades in glossy, matt and some with a sparkle finish. Embossed lettering may be a possibility as well. Copper letters may be an idea that works well also. These are just ideas rolling aroung in our heads but please give us your ideas*******
Reason: to give designers more time
This is for the 35+ year old woman.
Communication

```html
<!DOCTYPE html>
<html lang="en">
<head>
<meta charset="utf-8">
<title>Velmora Serum Box Panels</title>
<link href="https://fonts.googleapis.com/css2?family=Montserrat:wght@300;700&display=swap" rel="stylesheet">
<style>
  :root {
    --violet-deep: #3e3766;
    --violet: #5a5190;
    --violet-light: #7a71ad;
    --gold-dark: #8a5a14;
    --gold: #c8912e;
    --gold-light: #f0cc7a;
    --silver-dark: #9a9a9e;
    --silver: #d4d4d8;
    --silver-light: #ffffff;
    --copper-dark: #9c5a34;
    --copper: #cf8c61;
    --copper-light: #f6d2b8;
    --label-white: #ffffff;
    --paper: #ffffff;
  }
  * { margin: 0; padding: 0; box-sizing: border-box; }
  html, body { width: 685px; height: 1200px; overflow: hidden; background: var(--paper); }
  .sheet { position: relative; width: 685px; height: 1200px; }
  .defs { position: absolute; width: 0; height: 0; }
  .box-panel { position: absolute; width: 181px; height: 520px; overflow: hidden; }
  .box-panel svg.panel-art { position: absolute; inset: 0; width: 100%; height: 100%; }
  .brand-name {
    position: absolute; top: 58px; left: 50%; transform: translateX(-50%);
    writing-mode: vertical-rl;
    font-family: "Montserrat", sans-serif; font-weight: 300;
    font-size: 40px; letter-spacing: 4px; line-height: 1;
    color: var(--label-white);
  }
  .product-name {
    position: absolute; top: 432px; left: 0; width: 100%;
    text-align: center;
    font-family: "Montserrat", sans-serif; font-weight: 700;
    font-size: 12.5px; line-height: 1.2; letter-spacing: -0.2px;
    color: var(--label-white);
  }
  .row-metal .brand-name, .row-metal .product-name { color: var(--violet-deep); }
  .row-metal .product-name { top: 1028px; }
  .col-1 { left: 36px; } .col-2 { left: 252px; } .col-3 { left: 469px; }
  .row-violet { top: 55px; }
  .row-metal { top: 640px; }
  .row-metal .product-name { top: 390px; }
</style>
</head>
<body>
<main class="sheet">

  <svg class="defs" aria-hidden="true">
    <defs>
      <radialGradient id="violet-field" cx="50%" cy="38%" r="70%">
        <stop offset="0" style="stop-color:var(--violet-light)"/>
        <stop offset="0.6" style="stop-color:var(--violet)"/>
        <stop offset="1" style="stop-color:var(--violet-deep)"/>
      </radialGradient>
      <linearGradient id="violet-band" x1="0" y1="0" x2="1" y2="1">
        <stop offset="0" style="stop-color:var(--violet)"/>
        <stop offset="1" style="stop-color:var(--violet-deep)"/>
      </linearGradient>
      <radialGradient id="gold-field" cx="50%" cy="45%" r="70%">
        <stop offset="0" style="stop-color:var(--gold-light)"/>
        <stop offset="0.55" style="stop-color:var(--gold)"/>
        <stop offset="1" style="stop-color:var(--gold-dark)"/>
      </radialGradient>
      <radialGradient id="silver-field" cx="50%" cy="45%" r="70%">
        <stop offset="0" style="stop-color:var(--silver-light)"/>
        <stop offset="0.6" style="stop-color:var(--silver)"/>
        <stop offset="1" style="stop-color:var(--silver-dark)"/>
      </radialGradient>
      <radialGradient id="copper-field" cx="50%" cy="45%" r="70%">
        <stop offset="0" style="stop-color:var(--copper-light)"/>
        <stop offset="0.55" style="stop-color:var(--copper)"/>
        <stop offset="1" style="stop-color:var(--copper-dark)"/>
      </radialGradient>
      <linearGradient id="gold-sweep" x1="0" y1="0" x2="1" y2="0.4">
        <stop offset="0" style="stop-color:var(--gold-dark)"/>
        <stop offset="0.55" style="stop-color:var(--gold)"/>
        <stop offset="0.8" style="stop-color:var(--gold-light)"/>
        <stop offset="1" style="stop-color:var(--gold)"/>
      </linearGradient>
      <linearGradient id="silver-sweep" x1="0" y1="0" x2="1" y2="0.4">
        <stop offset="0" style="stop-color:var(--silver-dark)"/>
        <stop offset="0.55" style="stop-color:var(--silver)"/>
        <stop offset="0.8" style="stop-color:var(--silver-light)"/>
        <stop offset="1" style="stop-color:var(--silver)"/>
      </linearGradient>
      <linearGradient id="copper-sweep" x1="0" y1="0" x2="1" y2="0.4">
        <stop offset="0" style="stop-color:var(--copper-dark)"/>
        <stop offset="0.55" style="stop-color:var(--copper)"/>
        <stop offset="0.8" style="stop-color:var(--copper-light)"/>
        <stop offset="1" style="stop-color:var(--copper)"/>
      </linearGradient>
    </defs>
  </svg>

  <!-- Violet boxes with metallic base -->
  <section class="box-panel row-violet col-1">
    <svg class="panel-art" viewBox="0 0 181 520" preserveAspectRatio="none">
      <rect width="181" height="520" fill="url(#violet-field)" role="img" aria-label="Soft violet diamond-pattern background"/>
      <path d="M0 430 C30 470 90 505 181 405 L181 520 L0 520 Z" fill="url(#gold-sweep)"/>
      <path d="M40 520 C100 500 150 460 181 420 L181 440 C150 480 110 510 70 520 Z" fill="var(--gold-light)" opacity="0.7"/>
    </svg>
    <div class="brand-name">VELMORA</div>
    <p class="product-name">Vitamin C<br>Serum</p>
  </section>

  <section class="box-panel row-violet col-2">
    <svg class="panel-art" viewBox="0 0 181 520" preserveAspectRatio="none">
      <rect width="181" height="520" fill="url(#violet-field)" role="img" aria-label="Soft violet diamond-pattern background"/>
      <path d="M0 430 C30 470 90 505 181 405 L181 520 L0 520 Z" fill="url(#silver-sweep)"/>
      <path d="M40 520 C100 500 150 460 181 420 L181 440 C150 480 110 510 70 520 Z" fill="var(--silver-light)" opacity="0.8"/>
    </svg>
    <div class="brand-name">VELMORA</div>
    <p class="product-name">Anti Aging<br>Serum</p>
  </section>

  <section class="box-panel row-violet col-3">
    <svg class="panel-art" viewBox="0 0 181 520" preserveAspectRatio="none">
      <rect width="181" height="520" fill="url(#violet-field)" role="img" aria-label="Soft violet diamond-pattern background"/>
      <path d="M0 430 C30 470 90 505 181 405 L181 520 L0 520 Z" fill="url(#copper-sweep)"/>
      <path d="M40 520 C100 500 150 460 181 420 L181 440 C150 480 110 510 70 520 Z" fill="var(--copper-light)" opacity="0.8"/>
    </svg>
    <div class="brand-name">VELMORA</div>
    <p class="product-name">Anti Aging<br>Serum</p>
  </section>

  <!-- Metallic boxes with violet base -->
  <section class="box-panel row-metal col-1">
    <svg class="panel-art" viewBox="0 0 181 520" preserveAspectRatio="none">
      <rect width="181" height="520" fill="url(#gold-field)" role="img" aria-label="Soft gold diamond-pattern background"/>
      <path d="M0 445 C40 490 110 505 181 405 L181 520 L0 520 Z" fill="url(#violet-band)"/>
    </svg>
    <div class="brand-name">VELMORA</div>
    <p class="product-name">Vitamin C<br>Serum</p>
  </section>

  <section class="box-panel row-metal col-2">
    <svg class="panel-art" viewBox="0 0 181 520" preserveAspectRatio="none">
      <rect width="181" height="520" fill="url(#silver-field)" role="img" aria-label="Soft silver diamond-pattern background"/>
      <path d="M0 445 C40 490 110 505 181 405 L181 520 L0 520 Z" fill="url(#violet-band)"/>
    </svg>
    <div class="brand-name">VELMORA</div>
    <p class="product-name">Anti Aging<br>Serum</p>
  </section>

  <section class="box-panel row-metal col-3">
    <svg class="panel-art" viewBox="0 0 181 520" preserveAspectRatio="none">
      <rect width="181" height="520" fill="url(#copper-field)" role="img" aria-label="Soft copper diamond-pattern background"/>
      <path d="M0 445 C40 490 110 505 181 405 L181 520 L0 520 Z" fill="url(#violet-band)"/>
    </svg>
    <div class="brand-name">VELMORA</div>
    <p class="product-name">Anti Aging<br>Serum</p>
  </section>

</main>
</body>
</html>
```